Yoga site design

we need to design a homepage and content sections for our yoga portal

Palvenora

Palvenora is a yoga community ecosystem dedicated to the yoga enthusiasts and adopters of an active lifestyle based upon yoga and ayurvedic living. The objective of Palvenora is to expand the involvment and adoption of yoga across the communities and facilitate the profitable growth of the various stakeholders and service providers involved with the ecosystem

Site descriptor

The site will have 4 building blocks/functionalities as specified below;

1.Directory functionality wherein it would list yoga classes/events/ workshop/ retreats and show calendar by dates and place
1. when
2. where
3. what
4. who
5. cost
6. durations

2.Search functionality

a.Find a yoga class/studio close to you (location tagging/Mapleway maps)
search/show by studioname/ teacher/ Private sessions/ yoga family
1. when
2. where
3. what
4. who
5. cost

3.Content publishing capabilty

a.Micro sites studio directory/ teachers/ frequent event holders/ therapists - contributors and serviceproviders
1. words of descriprion about yourself and your business
2. an email address
3. a live web link
4. Mapleway maps
5. contact phone number
6. a logo upload
7. a picture of themselves, (we need to specify size)
8 Weekly/monthly calendar - where thay are and when

b.Topical content
• columns written by a refference or celebrity
• parts in Montly newsletter and/or downloadable

c.Monthly Newsletter

d.What is New/News/Flash Happenings on the Site

e.Community Board
a virtual meeting place on a login and username basis
• Twitter
• chat
• yoganetwork - offline community build
• find a group close to you!

4.E-commerce capability (Yoga store)
by category;
• yoga props
• yoga clothes
• Ayurvedic related products
• Books/Music/dvd
• skin/body
tickets to events -

yoga enthusiasts across multiple cities in europe and americas

• the design should not be intrusive and allow for multiple city instances to be created using the same deisgn sensibilities
• i do not need any tech coding.

```html
<!DOCTYPE html>
<html lang="en">
<head>
<meta charset="utf-8">
<title>Palvenora – Yoga Portal</title>
<link href="https://fonts.googleapis.com/css2?family=Source+Sans+3:wght@400;600&display=swap" rel="stylesheet">
<style>
:root{
  --page:#e9f0fa;
  --panel:#f3f7fc;
  --green:#6a9a1f;
  --green-light:#a9cd63;
  --green-dark:#5a8a1c;
  --text:#2b2b2b;
  --muted:#8a8a8a;
  --dots:#c5c9cf;
  --frame:#c3cbd6;
}
*{box-sizing:border-box;margin:0;padding:0}
html,body{width:1109px;height:1200px;overflow:hidden}
body{background:var(--page);font-family:"Source Sans 3",Arial,sans-serif;color:var(--text);position:relative}
.panel{position:absolute;left:181px;top:0;width:747px;height:1066px;background:var(--panel);box-shadow:0 0 18px rgba(120,140,170,.18)}
.abs{position:absolute}
.search-label{left:245px;top:15px;font-size:18px;color:var(--green)}
.search-box{left:304px;top:15px;width:262px;height:26px;background:#fff;border:1px solid #d9dee5;border-radius:4px;box-shadow:inset 0 1px 2px rgba(0,0,0,.12)}
.search-box svg{position:absolute;right:6px;top:3px}
.brand{left:776px;top:10px;display:flex;align-items:center;gap:7px;font-size:27px;line-height:32px;color:var(--green)}
.brand-dot{width:10px;height:10px;border-radius:50%;background:var(--green)}
.nav{left:197px;top:55px;width:713px;height:33px;border-radius:3px;background:linear-gradient(#c7e08f,#83b437 55%,#79aa2d);border:1px solid #9cc55a;display:flex;align-items:center}
.nav a{color:#fff;text-decoration:none;font-size:14px;text-align:center}
.nav .home{margin-left:4px;width:101px;height:26px;line-height:26px;background:linear-gradient(#e5f0cf,#c3dc93);border-radius:3px;color:#1d1d1d}
.hero{left:197px;top:90px;width:713px;height:330px;background:linear-gradient(#aac8ea 0%,#dde9f4 55%,#c8d6a2 75%,#6f922d 100%);box-shadow:0 14px 16px -10px rgba(0,0,0,.35)}
.hero-caption{left:240px;top:199px;font-size:18.5px;line-height:24px;color:#111}
.arrow{width:30px;height:30px;border-radius:50%;background:#c9dcb3;top:220px}
.arrow svg{position:absolute;left:7px;top:7px}
.heading{font-size:19px;font-weight:400;color:var(--green);display:flex;align-items:center;gap:7px;white-space:nowrap}
.heading i{display:block;width:10px;height:10px;border-radius:50%;background:var(--green)}
.copy{font-size:10.2px;line-height:15.7px;color:var(--text)}
.classes-figure{left:475px;top:635px;width:178px;height:161px;background:var(--frame)}
.classes-photo{position:absolute;left:6px;top:5px;width:166px;height:126px;background:linear-gradient(135deg,#d9d2c4,#8d8f9c 60%,#4f6f96)}
.classes-figure span{position:absolute;left:0;right:0;top:138px;text-align:center;font-size:13px;color:#3b3b3b}
.product{top:838px;width:132px;height:105px;background:#fff;border:1px solid #c9c9c9;box-shadow:0 1px 3px rgba(0,0,0,.25);padding:5px}
.product div{width:100%;height:100%}
.p1 div{background:radial-gradient(circle at 50% 45%,#c9c3d6,#7b7c96 60%,#f4f4f4 62%)}
.p2 div{background:linear-gradient(90deg,#e9d8c3,#c8a36b 50%,#7a4f8e)}
.p3 div{background:linear-gradient(135deg,#c7b3e0,#8e63b9 55%,#efe6f3)}
.readmore{left:570px;top:1020px;width:68px;height:16px;border-radius:8px;background:linear-gradient(#eef5e0,#d3e6ad);border:1px solid #c0d995;font-size:9px;color:#557d1a;text-align:center;line-height:14px;text-decoration:none}
.divider{left:663px;top:480px;width:1px;height:407px;background:#d3d8df}
.dir-list{left:686px;top:505px;width:203px;list-style:none}
.dir-list li{height:31.6px;border-bottom:1px dotted var(--dots);display:flex;align-items:center;gap:19px;font-size:13.5px;color:var(--muted)}
.map{left:684px;top:723px;width:225px;height:189px;border:1px solid #c8c8c8;background:linear-gradient(135deg,#e7e2d6,#ddd6c7);border-radius:2px}
.fold{top:1050px;width:17px;height:16px;background:#6c9a2a}
.fold.l{left:164px;clip-path:polygon(100% 0,100% 100%,0 100%)}
.fold.r{left:928px;clip-path:polygon(0 0,100% 100%,0 100%)}
.footer{left:164px;top:1065px;width:781px;height:50px;background:linear-gradient(#7dae32,#a8cc6a);box-shadow:0 6px 8px -4px rgba(0,0,0,.25);text-align:center;font-size:8px;line-height:50px;color:#2f3a1c}
</style>
</head>
<body>
<div class="panel"></div>

<header>
  <label class="abs search-label" for="q">Search</label>
  <div class="abs search-box">
    <svg width="22" height="20" viewBox="0 0 22 20"><circle cx="8" cy="8" r="5.5" fill="none" stroke="#6a9a1f" stroke-width="2.4"/><line x1="12" y1="12" x2="18" y2="17" stroke="#6a9a1f" stroke-width="3" stroke-linecap="round"/></svg>
  </div>
  <div class="abs brand"><span class="brand-dot"></span>Palvenora</div>
  <nav class="abs nav">
    <a class="home" href="#">Home</a>
    <a href="#" style="width:170px">About Us</a>
    <a href="#" style="width:125px">Classes</a>
    <a href="#" style="width:160px">Events</a>
    <a href="#" style="width:170px">Workshop</a>
  </nav>
</header>

<section>
  <div class="abs hero" role="img" aria-label="Woman in white holding a balanced yoga pose in a flowering meadow under a blue sky"></div>
  <p class="abs hero-caption">Contrary to popular belief, Lorem<br>Ipsum is not simply random text.</p>
  <div class="abs arrow" style="left:190px"><svg width="16" height="16" viewBox="0 0 16 16"><path d="M10 2 4 8l6 6" fill="none" stroke="#fff" stroke-width="3"/></svg></div>
  <div class="abs arrow" style="left:893px"><svg width="16" height="16" viewBox="0 0 16 16"><path d="M6 2l6 6-6 6" fill="none" stroke="#fff" stroke-width="3"/></svg></div>
</section>

<main>
  <h2 class="abs heading" style="left:202px;top:463px"><i></i>Welcome To Our Website</h2>
  <p class="abs copy" style="left:210px;top:497px;width:440px">Lorem Ipsum is simply dummy text of the printing and typesetting industry. Lorem Ipsum has been the industry's standard dummy text ever since the 1500s, when an unknown printer took a galley of type and scrambled it to make a type specimen book. It has survived not only five centuries, but also the leap into electronic typesetting, remaining essentially unchanged. It was popularised in the 1960s with the release of Letraset sheets containing Lorem Ipsum passages, and more recently with desktop publishing.</p>

  <h2 class="abs heading" style="left:202px;top:615px"><i></i>Yoga Classess</h2>
  <p class="abs copy" style="left:215px;top:649px;width:240px">Lorem Ipsum is simply dummy text of the printing and typesetting industry. Lorem Ipsum has been the industry's standard dummy text ever since the 1500s, when an unknown printer took a galley of type and scrambled it to make a type specimen book. It has survived not only five centuries, but also the leap into electronic typesetting, remaining essspassages, and more recently with desktop publishing.</p>
  <figure class="abs classes-figure">
    <div class="classes-photo" role="img" aria-label="Group of women seated cross-legged in a bright yoga class"></div>
    <span>Yoga Class</span>
  </figure>

  <h2 class="abs heading" style="left:202px;top:795px"><i></i>Yoga Store</h2>
  <div class="abs product p1" style="left:224px"><div role="img" aria-label="Yoga video game disc with a woman in a seated pose"></div></div>
  <div class="abs product p2" style="left:367px"><div role="img" aria-label="Heated flow yoga class DVD cover"></div></div>
  <div class="abs product p3" style="left:508px"><div role="img" aria-label="Full practice yoga DVD cover in purple tones"></div></div>
  <p class="abs copy" style="left:223px;top:959px;width:430px">Lorem Ipsum is simply dummy text of the printing and typesetting industry. Lorem Ipsum has been the industry's standard dummy text ever since the 1500s, when an unknown printer took a galley of type and scrambled it to make a type specimen book. It has survived not only five centuries.</p>
  <a class="abs readmore" href="#">Readmore....</a>
</main>

<div class="abs divider"></div>

<aside>
  <h2 class="abs heading" style="left:682px;top:462px"><i></i>Directory Functionality</h2>
  <ul class="abs dir-list">
    <li><svg width="18" height="12" viewBox="0 0 18 12"><path d="M1 1l5 5-5 5M8 1l5 5-5 5" fill="none" stroke="#8a8a8a" stroke-width="2.5"/></svg>Generators</li>
    <li><svg width="18" height="12" viewBox="0 0 18 12"><path d="M1 1l5 5-5 5M8 1l5 5-5 5" fill="none" stroke="#8a8a8a" stroke-width="2.5"/></svg>Reasonable.</li>
    <li><svg width="18" height="12" viewBox="0 0 18 12"><path d="M1 1l5 5-5 5M8 1l5 5-5 5" fill="none" stroke="#8a8a8a" stroke-width="2.5"/></svg>Characteristic</li>
    <li><svg width="18" height="12" viewBox="0 0 18 12"><path d="M1 1l5 5-5 5M8 1l5 5-5 5" fill="none" stroke="#8a8a8a" stroke-width="2.5"/></svg>Classical</li>
    <li><svg width="18" height="12" viewBox="0 0 18 12"><path d="M1 1l5 5-5 5M8 1l5 5-5 5" fill="none" stroke="#8a8a8a" stroke-width="2.5"/></svg>Virginia</li>
  </ul>
  <h2 class="abs heading" style="left:682px;top:685px"><i></i>Mapleway maps</h2>
  <div class="abs map" role="img" aria-label="Street map showing the studio location with a red pin"></div>
</aside>

<div class="abs fold l"></div>
<div class="abs fold r"></div>
<footer class="abs footer">Copyright (c) 2011. All rights reserved.www.palvenora.example</footer>
</body>
</html>
```